WinterCommuters

First, let me apologize for the short term. We just got an opportunity to place an ad in a commuter newspaper that will run throughout the winter months. We have tropical vacation rentals in Mexico, so it seems worth a shot.

We want to emphasize tropical luxury at competitive prices. Because we will be new to the audience, we need to cover a lot in one ad - images can definitely help. We are supplying photographs - feel free to crop or whatever.

We have the only private complex of luxury houses on the Mexican Caribbean coast, the "Riviera Maya" so we can accommodate anywhere from a single couple to a full wedding party. We want to show our large capacity without scaring off the single couple or small family with mom, dad, and a couple of kids.
Updates

Correction to text:  third paragraph.  The word should be "you", not "so" after "Riviera Maya,"
"As we are in the heart of the Riviera Maya, you will have "

Target Market(s)

Professionals looking to get out of the winter cold. Think tropical!

Industry/Entity Type

Wedding

Requirements
Must have
• The ad must be 5"x5" at 200 DPI (1,000 x 1000 pixels).
• The primary ad will be printed in black and white so it should be saved as a grayscale image. (I think they actually want a jpg, although a tiff would seem more logical!)
• The add will also be on the web in full color so please design the ad with color in mind and then change to grayscale after the content ends.
• Include our logo, phone number, e-mail, and website.
• Also, unless there is a good reason not to, include the four "first tier" images.
• Use the text as provided - not that some is optional.
Nice to have
• Please see the text in the attachments. OOPS: I downloaded the wrong version first - use the most recent "chicagoad" text!
• Also, unless there is a strong reason, use the "first tier" photos. We want to emphasize the accommodations, but also show large groups. We don't want to scare off the smaller groups (couples, small families) with the impression that we are only for large groups.
• The "second tier" photos are available if they would help. Both accommodation and weddings/large groups.
Should not have
• Stock photographs.
• I have (obviously) had some issues loading my files so please forgive the duplicates.

```html
<!DOCTYPE html>
<html lang="en">
<head>
<meta charset="utf-8">
<title>Casa Tortuga – Winter Commuter Ad</title>
<link href="https://fonts.googleapis.com/css2?family=Nunito:wght@800;900&family=Open+Sans:wght@400;600&display=swap" rel="stylesheet">
<style>
  :root{
    --page:#e6e2da;
    --header:#121212;
    --title-top:#7ff0ff;
    --title-bottom:#3fc6e6;
    --body-blue:#1438c8;
    --ink:#111111;
    --frame:#ffffff;
    --sun-yellow:#fff27a;
    --sun-orange:#f5a11a;
    --sun-red:#d8200c;
    --sea:#8fd3e0;
  }
  *{margin:0;padding:0;box-sizing:border-box}
  html,body{width:1200px;height:900px;overflow:hidden;background:var(--page)}
  .ad{
    position:absolute;left:160px;top:24px;width:880px;height:852px;
    overflow:hidden;font-family:"Open Sans",Verdana,sans-serif;
    background:linear-gradient(180deg,#cfeff6 0%,#e7f6f2 40%,#f7f6cf 62%,#fff7a6 80%,#fff6b8 100%);
  }
  .ad__backdrop{position:absolute;inset:0}
  .ad__header{
    position:absolute;left:0;top:0;width:880px;height:123px;background:var(--header);
  }
  .ad__title{
    position:absolute;left:53px;top:24px;
    font-family:"Nunito",Arial,sans-serif;font-weight:900;font-size:34px;line-height:38px;
    letter-spacing:-0.3px;
    background:linear-gradient(180deg,var(--title-top),var(--title-bottom));
    -webkit-background-clip:text;background-clip:text;color:transparent;
  }
  .copy{position:absolute;left:53px;color:var(--body-blue)}
  .copy--lead{top:161px;font-size:17.5px;line-height:21px;font-weight:600}
  .copy--detail{top:234px;font-size:11px;line-height:12px}
  .copy--questions{top:292px;font-size:11px;line-height:12px}
  .copy--homes{top:328px;font-size:17px;font-weight:600;color:var(--ink)}
  .copy--visit{top:358px;font-size:11.5px}
  .copy--facts{top:672px;font-size:14.5px;line-height:16px}
  .contact{position:absolute;left:53px;top:710px;font-size:18px;line-height:23px;font-weight:600;color:var(--ink)}
  .photo{position:absolute;border:3px solid var(--frame);box-shadow:0 1px 3px rgba(0,0,0,.35)}
  .photo--villa{left:56px;top:396px;width:250px;height:157px;background:linear-gradient(180deg,#8fc0e8,#c9b08a 55%,#6f5a3c)}
  .photo--wedding{left:314px;top:396px;width:248px;height:157px;background:linear-gradient(180deg,#4f8a3a,#6a9a4a 45%,#d9dccf 65%,#3e6a2a)}
  .photo--pool{left:570px;top:396px;width:247px;height:157px;background:linear-gradient(180deg,#6fb6ea,#bfe3f7 45%,#2e8a5a 60%,#28a8c8 80%,#c7a27a)}
  .photo--bedroom{left:56px;top:563px;width:183px;height:88px;background:linear-gradient(180deg,#f1ece2,#d6c6a8)}
  .photo--townhouses{left:250px;top:563px;width:181px;height:88px;background:linear-gradient(180deg,#a7c9e0,#b98e5a 50%,#3e5a2a)}
  .photo--patio{left:442px;top:563px;width:184px;height:88px;background:linear-gradient(180deg,#cfe4ef,#5a7a3a 55%,#4a3a26)}
  .photo--lounge{left:634px;top:563px;width:183px;height:88px;background:linear-gradient(180deg,#e9e3d6,#8a6a4a 60%,#3a2a1e)}
  .brand{
    position:absolute;right:34px;top:772px;display:flex;align-items:center;gap:6px;
    font-family:"Open Sans",Verdana,sans-serif;font-weight:600;font-size:15px;color:var(--body-blue);
  }
  .brand__dot{width:14px;height:14px;border-radius:50%;background:var(--body-blue)}
</style>
</head>
<body>
<main class="ad">
  <svg class="ad__backdrop" width="880" height="852" viewBox="0 0 880 852" aria-hidden="true">
    <defs>
      <linearGradient id="swoosh-warm" x1="0" x2="1">
        <stop offset="0" stop-color="var(--sun-red)"/>
        <stop offset=".5" stop-color="var(--sun-orange)"/>
        <stop offset="1" stop-color="var(--sun-red)"/>
      </linearGradient>
    </defs>
    <rect x="0" y="360" width="110" height="200" fill="var(--sea)" opacity=".5"/>
    <rect x="770" y="360" width="110" height="200" fill="var(--sea)" opacity=".5"/>
    <path d="M0 132 Q440 100 880 150 L880 122 L0 122Z" fill="var(--sun-yellow)"/>
    <path d="M0 150 Q440 108 880 176 L880 158 Q440 98 0 136Z" fill="url(#swoosh-warm)"/>
    <path d="M0 160 Q440 124 880 196 L880 186 Q440 118 0 154Z" fill="var(--sun-orange)" opacity=".6"/>
    <path d="M0 700 Q420 640 880 560 L880 600 Q420 690 0 740Z" fill="#fff3a0" opacity=".7"/>
    <path d="M0 808 Q440 790 880 832 L880 852 L0 852Z" fill="var(--sun-red)"/>
    <path d="M0 800 Q440 780 880 822 L880 832 Q440 790 0 808Z" fill="var(--sun-orange)"/>
    <path d="M0 790 Q440 768 880 812 L880 822 Q440 780 0 800Z" fill="var(--sun-yellow)"/>
  </svg>

  <header class="ad__header">
    <h1 class="ad__title">Vacations, Weddings, Reunions, Retreats<br>Wouldn't you rather be in a tropical paradise?</h1>
  </header>

  <p class="copy copy--lead">Come and relax in the only private complex of luxury houses on the beautiful<br>Mexican Riviera. Only 60 miles South of Cancun, we are a world apart<br>from the noise and crowds of large hotels and party towns.</p>
  <p class="copy copy--detail">Located in the quiet coastal village of Akumal, you get all of the best amenities, great restaurants<br>magnificent snorkeling and diving, beaches, and more in the laid back atmosphere that is so hard to find.<br>As we are in the heart of the Riviera Maya, you will have access to shopping<br>Mayan ruins, tourist attractions, golf, sailing, diving and much more.</p>
  <p class="copy copy--questions">Are you a couple looking for that perfect, secluded getaway?<br>Are you looking for a vacation in a quiet, safe, family-friendly area?<br>Do you have a family reunion, wedding, or retreat and you want everyone to be together?</p>
  <p class="copy copy--homes">With 5 luxury homes to choose from, we can meet your exact needs.</p>
  <p class="copy copy--visit">Visit our web site or call us directly.&nbsp; We look forward to hearing from you and to sharing our homes with you, your family and friends.</p>

  <div class="photo photo--villa" role="img" aria-label="Photo of the main villa with its stone tower and courtyard fountain"></div>
  <div class="photo photo--wedding" role="img" aria-label="Photo of an outdoor wedding ceremony with guests on the lawn"></div>
  <div class="photo photo--pool" role="img" aria-label="Photo of an infinity pool with palm trees by the lagoon"></div>
  <div class="photo photo--bedroom" role="img" aria-label="Photo of a bright bedroom"></div>
  <div class="photo photo--townhouses" role="img" aria-label="Photo of the townhouses among trees"></div>
  <div class="photo photo--patio" role="img" aria-label="Photo of a patio dining table overlooking the lagoon"></div>
  <div class="photo photo--lounge" role="img" aria-label="Photo of a furnished living room"></div>

  <p class="copy copy--facts">12 bedrooms, 15 beds, 17 bathrooms, and 5 pools.<br>Luxury Villas and Townhouses on Yal-Ku Lagoon, Akumal, Mexico</p>
  <p class="contact">Daniel &amp; Nora Pierce<br>(215) 555-0188 &nbsp;::&nbsp; info@CasaTortugaVillas.com</p>

  <div class="brand"><span class="brand__dot"></span>Casa Tortuga</div>
</main>
</body>
</html>
```